Create a new business card

I’m looking to update my business card to make it match the rest of my brand. I will include my current website as well as what my vehicle designs look like, etc..
What my business currently services
Weekly maintenance pool openings / closings
Equipment repair, including pumps, heaters, salt systems, filters, etc.
We install automatic covers and maintain them as well as provide preventative maintenance

I would like to include my name.
Darren Holcott.
My title
Owner
My email
Darren@tidewellnx.com
4015867120
Www.tidewellnx.com

```html
<!DOCTYPE html>
<html lang="en">
<head>
<meta charset="utf-8">
<title>Tidewell Pool Care — Business Card</title>
<link href="https://fonts.googleapis.com/css2?family=Lilita+One&family=Lato:wght@400&display=swap" rel="stylesheet">
<style>
  :root {
    --navy: #22336a;
    --orange: #e2622a;
    --sky: #2ab4e8;
    --white: #ffffff;
    --page: #eeeeef;
  }
  html, body {
    margin: 0;
    width: 1200px;
    height: 1200px;
    overflow: hidden;
    background: var(--page);
  }
  .card {
    position: absolute;
    left: 159px;
    width: 881px;
    height: 516px;
    box-shadow: 0 2px 6px rgba(0,0,0,0.18);
  }
  .card--front { top: 62px; }
  .card--back { top: 621px; }
  .card svg { display: block; width: 100%; height: 100%; }
  .display { font-family: "Lilita One", "Arial Rounded MT Bold", sans-serif; }
  .body { font-family: "Lato", Arial, sans-serif; }
</style>
</head>
<body>

<section class="card card--front" aria-label="Business card front">
  <svg viewBox="0 0 705 413" xmlns="http://www.w3.org/2000/svg">
    <rect class="card-base" width="705" height="413" fill="var(--white)"/>
    <path class="band-navy" d="M120 0 H705 V68 H440 C425 68 410 80 390 80 H300 Z" fill="var(--navy)"/>
    <path class="band-orange" d="M0 0 H125 C165 25 200 58 250 70 H322 Q333 70 331 82 H0 Z" fill="var(--orange)"/>
    <path class="band-divider" d="M125 0 C165 25 200 58 250 70 H322" fill="none" stroke="var(--white)" stroke-width="2"/>
    <path class="band-sky" d="M425 68 H705 V158 C610 132 510 104 472 82 Q455 70 425 68 Z" fill="var(--sky)"/>

    <g class="brand-name" text-anchor="middle">
      <circle cx="168" cy="232" r="9" fill="var(--orange)"/>
      <text class="display" x="168" y="276" font-size="34" fill="var(--navy)">Tidewell</text>
      <text class="display" x="168" y="312" font-size="34" fill="var(--navy)">Pool Care</text>
    </g>

    <g class="identity" text-anchor="end">
      <text class="display" x="656" y="239" font-size="36" fill="var(--navy)">Darren <tspan fill="var(--orange)">Holcott</tspan></text>
      <text class="display" x="656" y="269" font-size="24" fill="var(--navy)">Owner</text>
    </g>

    <g class="contacts body" text-anchor="end" font-size="16.5" fill="var(--navy)">
      <text x="628" y="311">4015867120</text>
      <text x="628" y="342">Darren@tidewellnx.com</text>
      <text x="628" y="367">www.tidewellnx.com</text>
    </g>

    <g class="contact-icons" fill="var(--navy)">
      <path class="icon-phone" d="M646 300 q-2 1 -1 4 q2 5 7 7 q3 1 4 -1 l-2 -2 q-1 1 -2 0 q-3 -2 -4 -4 q-1 -1 0 -2 z"/>
      <g class="icon-mail">
        <rect x="645" y="334" width="11" height="8"/>
        <path d="M645 334 L650.5 338.5 L656 334" fill="none" stroke="var(--white)" stroke-width="1"/>
      </g>
      <g class="icon-globe">
        <circle cx="650.5" cy="362" r="5.5"/>
        <path d="M645 362 H656 M650.5 356.5 Q647 362 650.5 367.5 Q654 362 650.5 356.5" fill="none" stroke="var(--white)" stroke-width="0.8"/>
      </g>
    </g>
  </svg>
</section>

<section class="card card--back" aria-label="Business card back">
  <svg viewBox="0 0 705 413" xmlns="http://www.w3.org/2000/svg">
    <defs>
      <clipPath id="card-clip"><rect width="705" height="413"/></clipPath>
    </defs>
    <rect class="card-base" width="705" height="413" fill="var(--navy)"/>
    <g clip-path="url(#card-clip)">
      <ellipse class="swoosh-sky" cx="345" cy="215" rx="390" ry="190" transform="rotate(-20 345 215)" fill="var(--sky)"/>
      <ellipse class="swoosh-orange" cx="370" cy="232" rx="390" ry="190" transform="rotate(-20 370 232)" fill="var(--orange)"/>
      <ellipse class="swoosh-white" cx="358" cy="228" rx="385" ry="186" transform="rotate(-20 358 228)" fill="var(--white)"/>
    </g>

    <g class="brand-name" text-anchor="middle">
      <circle cx="353" cy="172" r="9" fill="var(--orange)"/>
      <text class="display" x="353" y="216" font-size="34" fill="var(--navy)">Tidewell</text>
      <text class="display" x="353" y="252" font-size="34" fill="var(--navy)">Pool Care</text>
    </g>
  </svg>
</section>

</body>
</html>
```